Medical Billing Company Needs a Business Card Design

We need a business card design for a Florida based medical billing company called 'Medora Crestline Solutions'. We specialize in providing revenue cycle management services to physician and therapist offices (we're basically their back-office processing partner for providing billing software, claims submissions, A/R follow-up and patient statements & collections. Our logo is red and blue-ish, so make sure that whatever other elements are used will match appropriately. Our current business card design has a too small font size. I'd like to project an image that shows we are modern & reliable. On a side note, I'm planning on using ZIB for printing these cards.

Target Market(s)

Office managers, physicians, therapists

Industry/Entity Type

Printing

Requirements
Must have
• Logo
Name of Employee
Phone
Fax
E-mail
Website

```html
<!DOCTYPE html>
<html lang="en">
<head>
<meta charset="utf-8">
<title>Medora Crestline Solutions – Business Card</title>
<link rel="stylesheet" href="https://fonts.googleapis.com/css2?family=Jost:wght@400&family=Roboto+Condensed:wght@700&family=Open+Sans:wght@300;400&display=swap">
<style>
  :root {
    --stage: #2b2b2d;
    --paper: #ffffff;
    --navy: #2a2a78;
    --navy-deep: #1f1f5e;
    --royal: #3a3ab0;
    --glow: #7d86d8;
    --red: #a3151e;
    --grey: #8a8a8a;
    --ink-light: #eef0ff;
  }
  * { margin: 0; padding: 0; box-sizing: border-box; }
  html, body { width: 1200px; height: 713px; overflow: hidden; background: var(--stage); }
  .stage {
    width: 1200px; height: 713px;
    display: flex; align-items: center; justify-content: center; gap: 60px;
  }
  .card {
    position: relative; width: 520px; height: 297px; overflow: hidden;
    box-shadow: 0 12px 30px rgba(0,0,0,.45);
  }
  /* Front */
  .card--front { background: var(--paper); }
  .wordmark {
    font-family: "Jost", sans-serif; font-weight: 400;
    letter-spacing: 3px; text-transform: uppercase; white-space: nowrap;
  }
  .card--front .wordmark {
    position: absolute; top: 44px; left: 96px;
    font-size: 25px; color: var(--navy);
  }
  .person { position: absolute; top: 104px; left: 44px; }
  .person__name {
    font-family: "Roboto Condensed", sans-serif; font-weight: 700;
    font-size: 16px; color: var(--red);
  }
  .person__title {
    font-family: "Open Sans", sans-serif; font-weight: 400;
    font-size: 12px; color: var(--grey);
  }
  .contact {
    position: absolute; top: 140px; left: 250px; list-style: none;
    font-family: "Open Sans", sans-serif; font-weight: 300;
    font-size: 13px; line-height: 17px; color: #7a7a7a;
  }
  .contact li { display: flex; align-items: flex-start; gap: 9px; }
  .contact svg { flex: none; width: 12px; height: 12px; margin-top: 3px; fill: var(--navy); }
  .contact .no-icon { padding-left: 21px; }
  .front-bands { position: absolute; left: 0; bottom: 0; width: 520px; height: 46px; }
  /* Back */
  .card--back { background: var(--navy); }
  .back-field {
    position: absolute; inset: 0;
    background: radial-gradient(ellipse 60% 70% at 50% 42%, var(--glow) 0%, var(--royal) 45%, var(--navy) 100%);
  }
  .card--back .wordmark {
    position: absolute; top: 108px; left: 0; width: 100%; text-align: center;
    font-size: 27px; color: var(--ink-light);
  }
  .web {
    position: absolute; top: 178px; width: 100%; text-align: center;
    font-family: "Open Sans", sans-serif; font-weight: 400;
    font-size: 14px; color: var(--ink-light);
  }
</style>
</head>
<body>
<main class="stage">

  <section class="card card--front" aria-label="Card front">
    <div class="wordmark">Medora Crestline</div>

    <div class="person">
      <div class="person__name">Daniel Hartwell, CHBME</div>
      <div class="person__title">President</div>
    </div>

    <ul class="contact">
      <li>
        <svg viewBox="0 0 12 12" aria-hidden="true"><path d="M6 0a4 4 0 0 0-4 4c0 3 4 8 4 8s4-5 4-8a4 4 0 0 0-4-4zm0 5.6A1.6 1.6 0 1 1 6 2.4a1.6 1.6 0 0 1 0 3.2z"/></svg>
        <span>2180 SW Harbor Pine Rd,</span>
      </li>
      <li class="no-icon">Coral Bend, FL 34000</li>
      <li>
        <svg viewBox="0 0 12 12" aria-hidden="true"><path d="M1 4c0-2 2-3 5-3s5 1 5 3H8.5V3h-5v1zM2 5h8l1 6H1z"/></svg>
        <span>000.000.0000</span>
      </li>
      <li>
        <svg viewBox="0 0 12 12" aria-hidden="true"><path d="M3 0h6v4H3zM1 5h10v7H1zm2 2v1h2V7zm4 0v1h2V7z"/></svg>
        <span>000.000.0000</span>
      </li>
      <li>
        <svg viewBox="0 0 12 12" aria-hidden="true"><path d="M0 2h12v8H0zm1 1v.4l5 3.3 5-3.3V3z"/></svg>
        <span>info@medoracrestline.net</span>
      </li>
    </ul>

    <svg class="front-bands" viewBox="0 0 520 46" aria-hidden="true">
      <path d="M0 14 L360 14 L360 19 L0 19 Z" fill="var(--red)"/>
      <path d="M0 19 L362 19 C372 19 374 8 386 8 L520 8 L520 46 L0 46 Z" fill="var(--navy)"/>
    </svg>
  </section>

  <section class="card card--back" aria-label="Card back">
    <div class="back-field" role="img" aria-label="Deep blue background with a soft central glow and a faint repeating wave pattern"></div>
    <div class="wordmark">Medora Crestline</div>
    <div class="web">www.medoracrestline.net</div>
  </section>

</main>
</body>
</html>
```